Business Card for a recruitment agency specializing in engineers and geeks.

I am looking to create Business Card Design for my company.
That
## Company name:
Vornplick Inc.
Vornplick is a term coined from the following concepts.
1. geek + engineer
2. geek utopia
## Company Description:
The concept of the company is to be a recruitment agency that creates a paradise for geeky engineers. We want to be a place where engineers can have more freedom and ideal career support.
# Target.
The noun itself is often given to companies that want to hire engineers, geeks, and IT-related personnel, so it would be nice to get the impression that this company seems to have good engineers and IT personnel. There are many occasions where I meet with the human resources department, president, or senior management and give it to them.
# Atmosphere
We are happy with simplicity, but with an impact that will help people remember the company. The logo is based on a dinosaur that does programming, so it should be somewhat playful, but since it will basically be used in a business setting, please don't make it too silly.
# About the logo
See the attached files. The company logo represents our engineers smiling upward because of our work, with the motif of a dinosaur doing programming.
## Color
We will leave the color scheme to you, but since the logo is in black and white, colors with such a taste would fit well.
## file format
ai, psd, png, svg
Industry/Entity Type
human resource and employment agency
Contact Information for Business Card
Company name, address, email, tel, URL,logo
Colors
Designer to choose colors to be used in the design.
Look and feel
Each slider illustrates characteristics of the customer's brand and the style your logo design should communicate.

```html
<!DOCTYPE html>
<html lang="en">
<head>
<meta charset="utf-8">
<title>Vornplick Inc. – Business Card</title>
<link rel="stylesheet" href="https://fonts.googleapis.com/css2?family=Ubuntu:wght@400;500;700&display=swap">
<style>
  :root {
    --canvas: #e9e7e4;
    --card-dark: #1c1b1c;
    --card-dark-edge: #2a292a;
    --card-light: #ffffff;
    --card-light-shade: #ececec;
    --ink: #1a1a1a;
    --ink-soft: #6e6e6e;
    --ghost: #e4e4e4;
    --mark-on-dark: #5b5b5d;
    --rule: #3a3a3a;
  }
  * { box-sizing: border-box; margin: 0; padding: 0; }
  html, body {
    width: 1200px; height: 900px; overflow: hidden;
    background: var(--canvas);
    font-family: "Ubuntu", sans-serif;
    color: var(--ink);
  }
  .canvas { position: relative; width: 1200px; height: 900px; }

  .card {
    position: absolute; left: 280px;
    width: 640px; height: 366px;
    border-radius: 34px;
    overflow: hidden;
    box-shadow: 0 14px 30px rgba(0,0,0,.18);
  }

  /* back side */
  .card--back {
    top: 62px;
    background: linear-gradient(160deg, var(--card-dark-edge), var(--card-dark) 60%);
    display: flex; align-items: center; justify-content: center;
  }
  .back-mark {
    display: flex; align-items: center; gap: 14px;
    color: var(--mark-on-dark);
    font-weight: 700; font-size: 40px; letter-spacing: .5px;
  }
  .back-mark .square { width: 30px; height: 30px; background: var(--mark-on-dark); }

  /* front side */
  .card--front {
    top: 470px;
    background: linear-gradient(200deg, var(--card-light) 30%, var(--card-light-shade));
  }
  .ghost-name {
    position: absolute; left: 40px; bottom: 16px;
    font-size: 56px; font-weight: 700; color: var(--ghost);
    white-space: nowrap; line-height: 1;
  }
  .holder { position: absolute; left: 40px; top: 118px; }
  .holder-role { font-size: 15px; color: var(--ink-soft); }
  .holder-name { font-size: 17px; font-weight: 700; letter-spacing: .3px; margin-top: 1px; }

  .contacts {
    position: absolute; left: 330px; top: 36px;
    list-style: none; font-size: 15px; color: #2c2c2c;
  }
  .contacts li { display: flex; align-items: flex-start; gap: 10px; line-height: 19px; margin-bottom: 7px; }
  .contacts svg { width: 13px; height: 13px; margin-top: 3px; flex: none; fill: var(--ink); }

  .rule { position: absolute; right: 0; height: 1px; background: var(--rule); }
  .rule--top { top: 172px; width: 150px; }
  .rule--bottom { top: 226px; width: 300px; }

  .brand {
    position: absolute; right: 40px; top: 244px;
    display: flex; align-items: center; gap: 16px;
  }
  .brand .square { width: 46px; height: 46px; background: var(--ink); }
  .brand-name { font-size: 52px; font-weight: 500; color: var(--ink); line-height: 1; }
</style>
</head>
<body>
<main class="canvas">

  <section class="card card--back" aria-label="Card back">
    <div class="back-mark"><span class="square"></span><span>Vornplick</span></div>
  </section>

  <section class="card card--front" aria-label="Card front">
    <div class="ghost-name" aria-hidden="true">Vornplick</div>

    <div class="holder">
      <p class="holder-role">President</p>
      <p class="holder-name">DANA MORROW</p>
    </div>

    <ul class="contacts">
      <li>
        <svg viewBox="0 0 16 16" aria-hidden="true"><path d="M2 5c0-2 3-3 6-3s6 1 6 3v1h-3V5H5v1H2z M4 7h8l2 6H2z"/></svg>
        <span>(00) 0000 0000</span>
      </li>
      <li>
        <svg viewBox="0 0 16 16" aria-hidden="true"><path d="M1 3h14v10H1z M2 4l6 5 6-5" stroke="#fff" stroke-width="1.2"/></svg>
        <span>dana@vornplickinc.com</span>
      </li>
      <li>
        <svg viewBox="0 0 16 16" aria-hidden="true"><circle cx="8" cy="8" r="7"/><path d="M1 8h14M8 1c-3 4-3 10 0 14M8 1c3 4 3 10 0 14" stroke="#fff" fill="none"/></svg>
        <span>www.vornplickinc.com</span>
      </li>
      <li>
        <svg viewBox="0 0 16 16" aria-hidden="true"><path d="M8 1a5 5 0 0 1 5 5c0 4-5 9-5 9S3 10 3 6a5 5 0 0 1 5-5z"/><circle cx="8" cy="6" r="2" fill="#fff"/></svg>
        <span>11 dummy city, dummy place<br>P.O Box 0000 Dummy Land</span>
      </li>
    </ul>

    <div class="rule rule--top"></div>
    <div class="rule rule--bottom"></div>

    <div class="brand">
      <span class="square"></span>
      <span class="brand-name">Vornplick</span>
    </div>
  </section>

</main>
</body>
</html>
```